Facebook profile image design (Circle)

We require a Facebook profile image design for an event with a photo similar to the attached.

The event name is: Velmora Harbor Showcase & Gala 2022
Dat 7 - 8 October 2022

Colours: Gold, navy blue or black, white

file must be in pdf, png and ai

Target Market(s)

authors

Font styles to use
Serif

Requirements
Must have
• Author photo and book cover

```html
<!DOCTYPE html>
<html lang="en">
<head>
<meta charset="utf-8">
<title>Velmora Harbor Showcase &amp; Gala 2022 – Profile Badge</title>
<link rel="stylesheet" href="https://fonts.googleapis.com/css2?family=Montserrat:wght@600;700&family=Jost:wght@400&family=Cormorant+Garamond:wght@500;600&display=swap">
<style>
  :root{
    --gold:#d8b13c;
    --gold-deep:#b88a1f;
    --gold-light:#f0d66a;
    --navy:#0b1c3c;
    --white:#ffffff;
    --paper:#e6dccb;
    --ink:#1e2430;
  }
  html,body{margin:0;padding:0;width:1200px;height:1200px;overflow:hidden;background:var(--white);}
  .badge{display:block;width:1200px;height:1200px;}
  .event-date{font-family:"Montserrat",sans-serif;font-weight:700;font-size:64px;fill:var(--navy);}
  .brand-name{font-family:"Montserrat",sans-serif;font-weight:700;font-size:74px;fill:var(--gold);}
  .event-title{font-family:"Jost",sans-serif;font-weight:400;font-size:45px;fill:var(--white);}
  .event-year{font-family:"Montserrat",sans-serif;font-weight:700;font-size:112px;fill:var(--gold);}
  .cover-quote{font-family:"Montserrat",sans-serif;font-weight:600;font-size:7.5px;fill:var(--ink);}
  .cover-title{font-family:"Cormorant Garamond",serif;font-weight:600;font-size:34px;fill:#2a2620;}
  .cover-sub{font-family:"Montserrat",sans-serif;font-weight:600;font-size:7.5px;fill:var(--white);}
  .cover-author{font-family:"Cormorant Garamond",serif;font-weight:500;font-size:20px;fill:var(--white);}
  .star{fill:var(--gold);}
</style>
</head>
<body>
<svg class="badge" viewBox="0 0 1200 1200" xmlns="http://www.w3.org/2000/svg">
  <defs>
    <linearGradient id="ring-gold" x1="0" y1="0" x2="1" y2="1">
      <stop offset="0" stop-color="var(--gold-light)"/>
      <stop offset="0.5" stop-color="var(--gold)"/>
      <stop offset="1" stop-color="var(--gold-deep)"/>
    </linearGradient>
    <radialGradient id="inner-white" cx="0.45" cy="0.35" r="0.7">
      <stop offset="0" stop-color="#ffffff"/>
      <stop offset="1" stop-color="#e9e9ea"/>
    </radialGradient>
    <linearGradient id="portrait-tone" x1="0" y1="0" x2="0" y2="1">
      <stop offset="0" stop-color="#d9d6c9"/>
      <stop offset="0.45" stop-color="#b88a6c"/>
      <stop offset="1" stop-color="#5d6259"/>
    </linearGradient>
    <linearGradient id="cover-paper" x1="0" y1="0" x2="0" y2="1">
      <stop offset="0" stop-color="#ece4d4"/>
      <stop offset="0.6" stop-color="#d9ccb6"/>
      <stop offset="1" stop-color="#1a2238"/>
    </linearGradient>
    <linearGradient id="cover-photo" x1="0" y1="0" x2="0" y2="1">
      <stop offset="0" stop-color="#a98b74"/>
      <stop offset="1" stop-color="#1f2840"/>
    </linearGradient>
    <clipPath id="inner-circle"><circle cx="600" cy="600" r="568"/></clipPath>
    <path id="date-arc" d="M 96 436 A 530 530 0 0 1 781 102"/>
    <path id="star-shape" d="M0,-1 L0.235,-0.324 L0.951,-0.309 L0.381,0.124 L0.588,0.809 L0,0.4 L-0.588,0.809 L-0.381,0.124 L-0.951,-0.309 L-0.235,-0.324 Z"/>
  </defs>

  <circle class="frame-ring" cx="600" cy="600" r="590" fill="url(#ring-gold)"/>
  <circle class="frame-inner" cx="600" cy="600" r="568" fill="url(#inner-white)"/>

  <g clip-path="url(#inner-circle)">
    <g class="author-portrait" role="img" aria-label="Portrait photo of the author in a light headscarf and grey blazer">
      <path d="M 30 1100 L 30 790 Q 180 720 245 650 L 240 330 Q 420 150 600 300 L 625 650 Q 700 700 740 740 L 740 1100 Z" fill="url(#portrait-tone)"/>
    </g>
    <path class="navy-band" d="M 185 1015 C 420 800, 760 690, 1210 660 L 1210 1210 L -10 1210 Z" fill="var(--navy)"/>
    <path class="navy-band-edge" d="M 185 1015 C 420 800, 760 690, 1210 660" fill="none" stroke="var(--gold-light)" stroke-width="9"/>
  </g>

  <text class="event-date"><textPath href="#date-arc">7-8 October 2022</textPath></text>
  <g class="stars-top">
    <use href="#star-shape" class="star" transform="translate(598 82) scale(24)"/>
    <use href="#star-shape" class="star" transform="translate(663 80) scale(21)"/>
    <use href="#star-shape" class="star" transform="translate(720 88) scale(17)"/>
  </g>
  <g class="stars-left">
    <use href="#star-shape" class="star" transform="translate(94 492) scale(24)"/>
    <use href="#star-shape" class="star" transform="translate(80 560) scale(21)"/>
    <use href="#star-shape" class="star" transform="translate(80 620) scale(17)"/>
  </g>

  <g class="brand">
    <text class="brand-name" x="845" y="315" text-anchor="middle">VELMORA</text>
    <text class="brand-name" x="845" y="395" text-anchor="middle">HARBOR</text>
  </g>

  <g class="book">
    <rect class="book-pages" x="983" y="447" width="18" height="446" fill="#f3f1ec" stroke="#cfcac0" stroke-width="1"/>
    <rect class="book-cover" x="710" y="442" width="276" height="452" fill="url(#cover-paper)"/>
    <text class="cover-quote" x="848" y="470" text-anchor="middle">“You changed how I see every setback. Thank you, sister.”</text>
    <text class="cover-quote" x="848" y="481" text-anchor="middle">– Dr Lenora Quist, author of The Quiet Tide and</text>
    <text class="cover-quote" x="848" y="492" text-anchor="middle">Marisol's ‘all-time favourite guest’</text>
    <text class="cover-title" x="848" y="552" text-anchor="middle">EMBRACE YOUR</text>
    <text class="cover-title" x="848" y="590" text-anchor="middle">HURDLES</text>
    <g class="cover-photo" role="img" aria-label="Author photo on the book cover">
      <path d="M 732 835 L 732 790 Q 770 770 795 760 L 800 660 Q 850 600 900 660 L 905 760 Q 930 770 965 790 L 965 835 Z" fill="url(#cover-photo)"/>
    </g>
    <circle class="cover-badge" cx="938" cy="660" r="30" fill="var(--gold)"/>
    <text class="cover-sub" x="848" y="836" text-anchor="middle">HOW TO TURN ANY HURDLE INTO AN OPENING</text>
    <line x1="760" y1="842" x2="936" y2="842" stroke="var(--white)" stroke-width="1"/>
    <text class="cover-author" x="848" y="866" text-anchor="middle">NADIRA SOLVANE-REYES</text>
  </g>

  <g class="event-block">
    <text class="event-title" x="420" y="946">VELMORA</text>
    <text class="event-title" x="420" y="995">HARBOR</text>
    <text class="event-title" x="420" y="1044">SHOWCASE</text>
    <text class="event-title" x="420" y="1093">&amp; GALA</text>
    <text class="event-year" x="690" y="983">20</text>
    <text class="event-year" x="690" y="1090">22</text>
  </g>
</svg>
</body>
</html>
```